International Company needs a Letterhead & Envelope Design

Our Company name is Corvale Brightwick Limited.
We'd like to ask the Designers for the luxurious and sophisticated design. Our logo is very simple and neat with letter logos, so we look forward to more professional and refined designs from Designers.
We look forward to providing you with a great design.
Thanks very much in advance.

```html
<!DOCTYPE html>
<html lang="en">
<head>
<meta charset="utf-8">
<title>Corvale Brightwick Limited – Letterhead &amp; Envelopes</title>
<link rel="stylesheet" href="https://fonts.googleapis.com/css2?family=Roboto:wght@400;700&display=swap">
<style>
  :root {
    --backdrop: #d9d9d9;
    --paper: #f6f6f6;
    --ink-strong: #505050;
    --ink-body: #6e6e6e;
    --rule-light: #c8c8c8;
    --flap: #f1f1f1;
    --signature-tone: #e6e6e6;
  }
  * { box-sizing: border-box; margin: 0; padding: 0; }
  html, body { width: 1200px; height: 810px; overflow: hidden; }
  body {
    background: var(--backdrop);
    font-family: "Roboto", Arial, sans-serif;
    color: var(--ink-body);
    position: relative;
  }
  .sheet { position: absolute; background: var(--paper); }

  /* Letterhead */
  .letterhead { left: 137px; top: 110px; width: 436px; height: 614px; }
  .wordmark {
    position: absolute;
    font-weight: 700;
    color: var(--ink-strong);
    font-size: 17px;
    letter-spacing: 0.2px;
    white-space: nowrap;
  }
  .letterhead .wordmark { left: 34px; top: 62px; }
  .header-rule { position: absolute; left: 34px; top: 121px; width: 364px; height: 2px; background: var(--rule-light); }
  .header-rule::before { content: ""; position: absolute; left: 0; top: -0.5px; width: 127px; height: 3px; background: var(--ink-strong); }

  .contact { position: absolute; font-size: 7px; line-height: 10px; color: var(--ink-strong); }
  .letterhead .contact { left: 312px; top: 54px; }
  .contact .address { margin-bottom: 4px; }
  .contact .item { display: flex; align-items: center; gap: 3px; }
  .contact svg { width: 7px; height: 7px; fill: var(--ink-strong); flex: none; }

  .recipient { position: absolute; left: 35px; top: 206px; font-size: 7.5px; line-height: 11.5px; }
  .body-copy { position: absolute; left: 35px; width: 363px; font-size: 7.3px; line-height: 11.4px; text-align: justify; }
  .body-copy.first { top: 275px; }
  .body-copy.second { top: 378px; }
  .signature { position: absolute; left: 35px; top: 438px; width: 84px; height: 52px; background: var(--signature-tone); border-radius: 3px; }
  .sign-title { position: absolute; left: 35px; top: 503px; font-size: 7.3px; }

  /* Envelope back */
  .envelope-back { left: 619px; top: 193px; width: 444px; height: 222px; }
  .envelope-back .flap { position: absolute; left: 0; top: 0; width: 444px; height: 66px; }
  .envelope-back .wordmark { left: 0; right: 0; top: 24px; text-align: center; }

  /* Envelope front */
  .envelope-front { left: 618px; top: 444px; width: 445px; height: 221px; }
  .envelope-front .wordmark { left: 28px; top: 28px; }
  .envelope-front .contact { left: 28px; top: 74px; }
</style>
</head>
<body>

<section class="sheet letterhead" aria-label="Letterhead">
  <div class="wordmark">Corvale Brightwick</div>
  <address class="contact" style="font-style:normal">
    <div class="address">48 Harrowmere Rd.<br>Ste 310 Lindale, CA 90412</div>
    <div class="item"><svg viewBox="0 0 10 10"><path d="M2 0.5 L4 2.5 L3 4 Q4.5 6 6 7 L7.5 6 L9.5 8 L8 9.5 Q3 9 0.5 2 Z"/></svg>555-014-2290</div>
    <div class="item"><svg viewBox="0 0 10 10"><path d="M0.5 2 H9.5 V8.5 H0.5 Z M1 2.5 L5 5.5 L9 2.5" stroke="#fff" stroke-width="0.8"/></svg>hello@corvalebrightwick.com</div>
    <div class="item"><svg viewBox="0 0 10 10"><circle cx="5" cy="5" r="4.5"/><path d="M0.5 5 H9.5 M5 0.5 V9.5 M5 0.5 Q2 5 5 9.5 M5 0.5 Q8 5 5 9.5" stroke="#fff" stroke-width="0.6" fill="none"/></svg>www.corvalebrightwick.com</div>
  </address>
  <div class="header-rule"></div>

  <p class="recipient">Dear Halvorsen<br>Tessamere Print Works<br>Department Design</p>

  <p class="body-copy first">Lorem ipsum dolor sit amet, consectetuer adipiscing elit. Aenean commodo ligula eget dolor. Aenean massa. Cum sociis natoque penatibus et magnis dis parturient montes, nascetur ridiculus mus. Donec quam felis, ultricies nec, pellentesque eu, pretium quis, sem. Nulla consequat massa quis enim. Donec pede justo, fringilla vel, aliquet nec, vulputate eget, arcu. In enim justo, rhoncus ut, imperdiet a, venenatis vitae, justo. Nullam dictum felis eu pede mollis pretium. Integer tincidunt. Cras dapibus. Vivamus elementum semper nisi.Nullam dictum felis eu pede mollis pretium. Integer tincidunt. Cras dapibus. Vivamus elementum semper nisi.felis eu pede mollis pretium. Integer tincidunt. Cras dapibus.</p>

  <p class="body-copy second">Quisque rutrum. Aenean imperdiet. Etiam ultricies nisi vel augue. Curabitur ullamcorper ultricies nisi. Nam eget dui. Etiam rhoncus. Maecenas tempus, tellus eget condimentum rhoncus, sem quam semper libero, sit amet adipiscing sem neque sed ipsum.felis pede mollis pretium. I am tincidunt. Cras dapibus.</p>

  <div class="signature" role="img" aria-label="Handwritten signature of the director"></div>
  <p class="sign-title">Director/Excecutive Director</p>
</section>

<section class="sheet envelope-back" aria-label="Envelope back">
  <svg class="flap" viewBox="0 0 444 66" aria-hidden="true">
    <path d="M0 0 H444 L434 56 Q432 65 422 65 H22 Q12 65 10 56 Z" fill="var(--flap)" stroke="#dcdcdc" stroke-width="1"/>
  </svg>
  <div class="wordmark">Corvale Brightwick</div>
</section>

<section class="sheet envelope-front" aria-label="Envelope front">
  <div class="wordmark">Corvale Brightwick</div>
  <address class="contact" style="font-style:normal">
    <div class="address">48 Harrowmere Rd.<br>Ste 310 Lindale, CA 90412</div>
    <div class="item"><svg viewBox="0 0 10 10"><path d="M2 0.5 L4 2.5 L3 4 Q4.5 6 6 7 L7.5 6 L9.5 8 L8 9.5 Q3 9 0.5 2 Z"/></svg>555-014-2290</div>
    <div class="item"><svg viewBox="0 0 10 10"><path d="M0.5 2 H9.5 V8.5 H0.5 Z M1 2.5 L5 5.5 L9 2.5" stroke="#fff" stroke-width="0.8"/></svg>hello@corvalebrightwick.com</div>
    <div class="item"><svg viewBox="0 0 10 10"><circle cx="5" cy="5" r="4.5"/><path d="M0.5 5 H9.5 M5 0.5 V9.5 M5 0.5 Q2 5 5 9.5 M5 0.5 Q8 5 5 9.5" stroke="#fff" stroke-width="0.6" fill="none"/></svg>www.corvalebrightwick.com</div>
  </address>
</section>

</body>
</html>
```